Business Cards/Stationary/Letterhead for Crestline Weight Loss Center
Be Healthy, Be Fit, and Be Ready to Lose Weight!
Creative Brief
Simple
Derek Tolsan, PA
Physician Assistant, Co-founder
52816 Birchwood Lane Fremont, CA 94592-7731
CrestlineSlim@mailhaven.example
www.crestlineslim.example
Aim for Results with Crestline Weight Loss! HCG, Appetite Suppressants,B12/B-Complex injections, Menu Plans, Exercise Plans, Nutriceuticals, Supplements.
Present this card to a friend; If your friend signs up, you will receive a 20% discount. The referrals are endless. If you refer 5 friends who sign up then you will receive 100% discount on your next visit. Just make sure your friend puts your name down in the "referral" section of the information sheet and you will be that much closer to saving. (Discount will only apply to weight loss program, discount only applicable for one month or week supply of medication. Non-transferrable. Referral cannot be an existing patient.) Appointment Date: _________ Time: _____

```html
<!DOCTYPE html>
<html lang="en">
<head>
<meta charset="utf-8">
<title>Crestline Weight Loss Center — Business Card</title>
<link href="https://fonts.googleapis.com/css2?family=Open+Sans:wght@400;600;700&display=swap" rel="stylesheet">
<style>
  :root {
    --green: #7ab934;
    --green-dark: #5f9a22;
    --orange: #ef7d1a;
    --text-gray: #6b6b6b;
    --rule-gray: #cfcfcf;
    --card: #ffffff;
    --backdrop: #ebe8e3;
  }
  * { margin: 0; padding: 0; box-sizing: border-box; }
  html, body {
    width: 1200px; height: 914px; overflow: hidden;
    background: var(--backdrop);
    font-family: "Open Sans", Arial, sans-serif;
  }
  .card {
    position: absolute; left: 100px; top: 171px;
    width: 1000px; height: 572px;
    background: var(--card);
    box-shadow: 0 6px 24px rgba(0,0,0,0.12);
    overflow: hidden;
  }
  .brand {
    position: absolute; left: 270px; top: 92px;
    display: flex; align-items: center; gap: 18px;
  }
  .brand-dot {
    width: 74px; height: 74px; border-radius: 50%;
    background: var(--green);
    flex: none;
  }
  .brand-text { display: flex; flex-direction: column; }
  .brand-name {
    font-size: 34px; font-weight: 600; color: var(--green);
    letter-spacing: -0.3px; line-height: 1.1;
  }
  .brand-tagline {
    font-size: 10px; color: var(--text-gray);
    letter-spacing: 1.6px; margin-top: 4px;
  }
  .person {
    position: absolute; left: 0; width: 100%; top: 232px;
    text-align: center; padding-left: 110px;
  }
  .person-name { font-size: 24px; font-weight: 700; color: var(--orange); }
  .person-title { font-size: 19px; color: var(--green-dark); margin-top: 2px; }
  .address {
    position: absolute; right: 530px; top: 328px;
    text-align: right; font-size: 17px; line-height: 1.45; color: var(--text-gray);
  }
  .divider {
    position: absolute; left: 492px; top: 328px;
    width: 1px; height: 110px; background: var(--rule-gray);
  }
  .contacts {
    position: absolute; left: 512px; top: 326px;
    list-style: none; font-size: 15px; color: var(--text-gray);
  }
  .contacts li { display: flex; align-items: center; gap: 10px; height: 36px; }
  .contact-icon { width: 20px; height: 20px; flex: none; }
  .bands { position: absolute; left: 0; bottom: 0; width: 1000px; height: 130px; }
</style>
</head>
<body>
  <div class="card">
    <div class="brand">
      <span class="brand-dot"></span>
      <div class="brand-text">
        <span class="brand-name">Crestline Weight Loss Center</span>
        <span class="brand-tagline">THE SIMPLE WEIGHT LOSS PATH FOR EVERY BODY</span>
      </div>
    </div>

    <div class="person">
      <p class="person-name">Derek Tolsan, PA</p>
      <p class="person-title">Physician Assistant, Co-founder</p>
    </div>

    <address class="address" style="font-style:normal">
      52816 Birchwood Lane<br>
      Fremont, CA 94592-7731
    </address>

    <span class="divider"></span>

    <ul class="contacts">
      <li>
        <svg class="contact-icon" viewBox="0 0 20 20"><circle cx="10" cy="10" r="10" fill="var(--orange)"/><path d="M7 5.5l2 2-1.2 1.3c.7 1.4 1.6 2.3 3 3l1.3-1.2 2 2-1.3 1.6c-3.4-.4-6.7-3.7-7.1-7.1z" fill="#fff"/></svg>
        650-555-0143
      </li>
      <li>
        <svg class="contact-icon" viewBox="0 0 20 20"><circle cx="10" cy="10" r="10" fill="var(--orange)"/><rect x="5" y="6.5" width="10" height="7" fill="none" stroke="#fff" stroke-width="1.3"/><path d="M5 6.8l5 4 5-4" fill="none" stroke="#fff" stroke-width="1.3"/></svg>
        CrestlineSlim@mailhaven.example
      </li>
      <li>
        <svg class="contact-icon" viewBox="0 0 20 20"><circle cx="10" cy="10" r="10" fill="var(--orange)"/><circle cx="10" cy="10" r="5" fill="none" stroke="#fff" stroke-width="1.2"/><path d="M5 10h10M10 5c-2.4 3-2.4 7 0 10M10 5c2.4 3 2.4 7 0 10" fill="none" stroke="#fff" stroke-width="1"/></svg>
        www.crestlineslim.example
      </li>
    </ul>

    <svg class="bands" viewBox="0 0 1000 130" preserveAspectRatio="none">
      <line x1="0" y1="44" x2="1000" y2="44" stroke="var(--rule-gray)" stroke-width="1.5"/>
      <polygon points="0,44 560,44 520,86 0,86" fill="var(--green)"/>
      <polygon points="545,86 1000,86 1000,118 515,118" fill="var(--orange)"/>
    </svg>
  </div>
</body>
</html>
```